Copperkettle Menu

I want to re design my menu at our restaurant Copperkettle, the current menu and information about the restaurant is online at www.copperkettle-eatery.example.nz, have attached the logo for Copperkettle as well as the new menu specifications

Menu design Specifications
· Rustic

· Raw

· Unpolished

· Urban

```html
<!DOCTYPE html>
<html lang="en">
<head>
<meta charset="utf-8">
<title>Copperkettle Menu</title>
<link href="https://fonts.googleapis.com/css2?family=Pathway+Gothic+One&display=swap" rel="stylesheet">
<style>
  :root {
    --ink: #0b0b0c;
    --navy: #173a5c;
    --burlap: #b89a6a;
    --burlap-dark: #8c7249;
    --lime: #b6ea2a;
    --lime-dark: #86b414;
    --tape: #c9c9c9;
    --panel: #3b3739;
    --cream: #d8d4c8;
    --muted: #a3a2a8;
    --logo: #8d9196;
  }
  * { margin: 0; padding: 0; box-sizing: border-box; }
  html, body { width: 776px; height: 1200px; overflow: hidden; background: var(--ink); }
  body { font-family: "Pathway Gothic One", sans-serif; }
  .menu { position: relative; width: 776px; height: 1200px; background: var(--ink); overflow: hidden; }

  .brand { position: absolute; left: 69px; top: 22px; font-size: 36px; letter-spacing: 1px; color: var(--logo); text-transform: uppercase; }

  .band { position: absolute; background: var(--navy); }
  .band--snacks { left: 440px; top: 103px; width: 336px; height: 75px; }
  .band--sides { left: 0; top: 580px; width: 776px; height: 160px; }

  .strip { position: absolute; }
  .strip--snacks { left: 0; top: 80px; width: 460px; height: 108px; }
  .strip--sides { left: 344px; top: 584px; width: 432px; height: 136px; }

  .section-title { position: absolute; text-transform: uppercase; font-size: 24px; line-height: 28px; }
  .section-title--snacks { left: 72px; top: 120px; color: var(--cream); }
  .section-title--sides { left: 631px; top: 633px; color: var(--navy); }

  .list { position: absolute; list-style: none; }
  .list li { display: flex; height: 35.3px; align-items: center; font-size: 21px; }
  .list--snacks { left: 72px; top: 182px; width: 648px; color: var(--cream); }
  .list--snacks .price { margin-left: auto; width: 30px; text-align: right; }

  .panel { position: absolute; left: 0; top: 740px; width: 494px; height: 370px; background: var(--panel); }

  .size-head { position: absolute; top: 776px; font-size: 21px; color: var(--muted); width: 40px; text-align: center; }
  .size-head--sm { left: 601px; }
  .size-head--lg { left: 696px; }

  .list--sides { left: 77px; top: 811px; width: 650px; color: var(--muted); }
  .list--sides .name { width: 524px; }
  .list--sides .price { width: 40px; text-align: center; }
  .list--sides .price--lg { margin-left: 55px; }
</style>
</head>
<body>
<main class="menu">
  <h1 class="brand">Copperkettle</h1>

  <div class="band band--snacks"></div>
  <svg class="strip strip--snacks" viewBox="0 0 460 108" role="img" aria-label="Torn burlap strip taped to the board">
    <polygon points="0,8 60,4 140,10 220,5 300,9 380,4 430,8 430,98 380,102 300,97 220,103 140,98 60,104 0,100" fill="var(--burlap)"/>
    <rect x="142" y="0" width="82" height="28" fill="var(--tape)" opacity="0.55"/>
    <rect x="424" y="6" width="30" height="80" fill="var(--tape)" opacity="0.55"/>
  </svg>
  <h2 class="section-title section-title--snacks">Snacks</h2>

  <ul class="list list--snacks">
    <li><span class="name">Pork Crackling</span><span class="price">5</span></li>
    <li><span class="name">Pasties &amp; Plum Sauce</span><span class="price">12</span></li>
    <li><span class="name">Lamb Meat and Pomegrenate Mollases</span><span class="price">15</span></li>
    <li><span class="name">Pulled Pork &amp; Apple Slaw Sliders</span><span class="price">12</span></li>
    <li><span class="name">Cheese Fondue &amp; Asparagus</span><span class="price">10</span></li>
    <li><span class="name">Battered Fish Finger &amp; Tartare Sauce</span><span class="price">9</span></li>
    <li><span class="name">Hand Cut Fries &amp; Tomato Sauce</span><span class="price">7</span></li>
    <li><span class="name">Barbecued Chicken Tulips</span><span class="price">14</span></li>
    <li><span class="name">Steamed Mussels &amp; Tomato Salsa</span><span class="price">12</span></li>
    <li><span class="name">Garlic Bread</span><span class="price">6</span></li>
    <li><span class="name">Crispy Lentil Balls &amp; Roast Garlic Yoghurt</span><span class="price">8</span></li>
  </ul>

  <div class="band band--sides"></div>
  <svg class="strip strip--sides" viewBox="0 0 432 136" role="img" aria-label="Torn lime burlap strip taped to the board">
    <polygon points="12,14 90,10 170,16 250,11 330,15 432,12 432,116 330,120 250,114 170,121 90,115 12,119" fill="var(--lime)"/>
    <rect x="0" y="30" width="30" height="66" fill="var(--tape)" opacity="0.55"/>
    <rect x="268" y="0" width="84" height="30" fill="var(--tape)" opacity="0.55"/>
  </svg>
  <h2 class="section-title section-title--sides">Salads<br>&amp; Sides</h2>

  <div class="panel"></div>
  <span class="size-head size-head--sm">SM</span>
  <span class="size-head size-head--lg">LG</span>

  <ul class="list list--sides">
    <li><span class="name">Warmed Red Skinned Potatoes with Dill &amp; Mustard</span><span class="price">6</span><span class="price price--lg">9</span></li>
    <li><span class="name">Tomato &amp; Mixed Beans</span><span class="price">8</span><span class="price price--lg">11</span></li>
    <li><span class="name">Char Grilled Vegetables &amp; Halloumi</span><span class="price">7</span><span class="price price--lg">10</span></li>
    <li><span class="name">Orzo, Broad Bean &amp; Feta</span><span class="price">7</span><span class="price price--lg">10</span></li>
    <li><span class="name">Beetroot, Spinach &amp; Goats Cheese with Maple</span><span class="price">8</span><span class="price price--lg">11</span></li>
    <li><span class="name">Mixed Leaves &amp; Citrus Emulsion</span><span class="price">6</span><span class="price price--lg">9</span></li>
    <li><span class="name">Steamed Brocolli &amp; Sesame Butter</span><span class="price">6</span><span class="price price--lg">9</span></li>
  </ul>
</main>
</body>
</html>
```